Collectible Card Trading Company ~ Tidewell and Finch Collectibles

Business card design using the attached images as a reference point. The color pallet is the color choice I prefer. If you have any way of improving on the design that would be appreciated. This will be used as an insert for product shipments as well as at geekfair and other collectible trade shows so it needs to be eye catching and memorable. Anything that you can do to make my business POP with this business card would be appreciated.

Target Market(s)

Collectible card purchasers primarily but all collectors ingeneral

Industry/Entity Type

Retail

Contact Information for Business Card

Details are included on the provided images

Colors

Designer to choose colors to be used in the design.

Requirements
Must have
• Bold design
Nice to have
• N/A
Should not have
• N/A

```html
<!DOCTYPE html>
<html lang="en">
<head>
<meta charset="utf-8">
<title>Tidewell &amp; Finch Co. — Business Card</title>
<link rel="stylesheet" href="https://fonts.googleapis.com/css2?family=Oswald:wght@500;600&family=Montserrat:wght@700;800&display=swap">
<style>
  :root {
    --page: #f6f4ef;
    --navy: #1f2a3a;
    --navy-light: #2b3b4f;
    --gold: #b97a23;
    --gold-soft: #c99245;
    --white: #ffffff;
  }
  * { box-sizing: border-box; margin: 0; padding: 0; }
  html, body {
    width: 1200px;
    height: 1200px;
    overflow: hidden;
    background: var(--page);
  }
  .canvas {
    position: relative;
    width: 1200px;
    height: 1200px;
  }
  .card {
    position: absolute;
    width: 817px;
    height: 467px;
    border-radius: 36px;
    overflow: hidden;
  }

  /* Front */
  .card-front {
    left: 144px;
    top: 150px;
    background: radial-gradient(ellipse at 48% 55%, var(--navy-light) 0%, var(--navy) 70%);
    color: var(--gold);
  }
  .brand-name {
    position: absolute;
    left: 0;
    right: 0;
    top: 62px;
    text-align: center;
    font-family: "Oswald", sans-serif;
    font-weight: 600;
    font-size: 72px;
    line-height: 1;
    letter-spacing: 1px;
  }
  .mascot-art {
    position: absolute;
    left: 300px;
    top: 158px;
    width: 186px;
    height: 186px;
    border-radius: 50%;
    background: radial-gradient(circle at 50% 45%, #3a4250 0%, #5a4a32 100%);
  }
  .established {
    position: absolute;
    top: 290px;
    font-family: "Montserrat", sans-serif;
    font-weight: 800;
    font-size: 26px;
    line-height: 1;
  }
  .established-label { left: 148px; }
  .established-year { left: 575px; }
  .tagline {
    position: absolute;
    left: 0;
    right: 0;
    top: 380px;
    text-align: center;
    font-family: "Montserrat", sans-serif;
    font-weight: 800;
    font-size: 31px;
    line-height: 1;
  }

  /* Back */
  .card-back {
    left: 283px;
    top: 648px;
    background: var(--gold);
    color: var(--white);
    font-family: "Oswald", sans-serif;
    font-weight: 500;
  }
  .shop-link {
    position: absolute;
    left: 50%;
    top: 32px;
    transform: translate(-50%, -50%) rotate(180deg);
    white-space: nowrap;
    font-size: 21px;
    letter-spacing: 0.3px;
  }
  .social-links {
    position: absolute;
    left: 52px;
    top: 232px;
    transform: translate(-50%, -50%) rotate(90deg);
    white-space: nowrap;
    font-size: 21px;
    line-height: 26px;
  }
  .website {
    position: absolute;
    left: 784px;
    top: 235px;
    transform: translate(-50%, -50%) rotate(90deg);
    white-space: nowrap;
    font-size: 21px;
  }
  .person {
    position: absolute;
    left: 0;
    right: 0;
    top: 216px;
    text-align: center;
    font-family: "Montserrat", sans-serif;
    font-weight: 800;
    line-height: 1;
  }
  .person-name { font-size: 27px; }
  .person-role { font-size: 21px; margin-top: 10px; }
  .contact {
    position: absolute;
    left: 0;
    right: 0;
    top: 388px;
    text-align: center;
    font-size: 21px;
    line-height: 31px;
  }
</style>
</head>
<body>
  <main class="canvas">
    <section class="card card-front" aria-label="Business card front">
      <h1 class="brand-name">Tidewell &amp; Finch Co.</h1>
      <div class="mascot-art" role="img" aria-label="Roaring tiger head illustration in gold line art"></div>
      <p class="established established-label">est.</p>
      <p class="established established-year">2016</p>
      <p class="tagline">Cards &amp; Collectibles</p>
    </section>

    <section class="card card-back" aria-label="Business card back">
      <p class="shop-link">shopmart @ www.shopmart.com/str/tidewellfinch</p>
      <div class="social-links">
        <p>photogram @tidewellfinchco</p>
        <p>chirper @Tidewell_Finch</p>
      </div>
      <p class="website">www.tidewellfinchco.com</p>
      <div class="person">
        <p class="person-name">owen marlow</p>
        <p class="person-role">chief collector</p>
      </div>
      <div class="contact">
        <p>owen@tidewellfinchco.com</p>
        <p>harlow, vermont</p>
      </div>
    </section>
  </main>
</body>
</html>
```